a residential cleaning service needs a website

We need a website for our faith based residential cleaning service, we are called MARGOT'S CLEANING SERVICE. We want a website that is clean looking both for mobile version and desktop. We want to convey cleanliness and trust to our clients. The color scheme should go in hand with the colors of the LOGO. We would like an about page, statement of faith page, services page and also a page for a booking module that our CRM has provided for us to being able to code and dress said module is important. The website not only needs to market to new customers and convey our service but also be easy to use for existing clients to schedule cleanings and services.
Industry/Entity Type
Cleaning Service
Coding
Coded - Design and coding required
Number of Pages Required
4 page
Requirements
Must have
- About page
Statement of Faith page
services page
booking and login page

```html
<!DOCTYPE html>
<html lang="en">
<head>
<meta charset="utf-8">
<title>Margot's Cleaning Service</title>
<link rel="stylesheet" href="https://fonts.googleapis.com/css2?family=Poppins:wght@300;400;500;600&family=Oswald:wght@300;400&display=swap">
<style>
:root{
  --blue:#2447a0;
  --blue-soft:#3c63c4;
  --ink:#2b2b2d;
  --grey:#5d5d60;
  --muted:#77777a;
  --line:#3f3f42;
  --paper:#ffffff;
  --mist:#f3f3f4;
  --footer:#3a3a3d;
  --field:#e6e6e8;
}
*{box-sizing:border-box;margin:0;padding:0}
html,body{width:1200px;height:3306px;overflow:hidden}
body{position:relative;background:var(--paper);font-family:"Poppins",sans-serif;color:var(--ink)}
.abs{position:absolute}

/* header */
.site-header{position:absolute;left:0;top:0;width:1200px;height:120px;background:var(--paper)}
.brand{left:87px;top:34px;display:flex;align-items:center;gap:10px}
.brand-dot{width:40px;height:40px;border-radius:50%;background:var(--blue)}
.brand-name{font-size:15px;font-weight:600;color:var(--blue);line-height:1.15;width:120px}
.call{left:684px;top:28px;font-family:"Oswald",sans-serif;font-weight:300;font-size:17px;color:var(--ink);display:flex;align-items:center;gap:6px}
.call b{font-weight:400;color:var(--blue)}
.btn{display:flex;align-items:center;justify-content:center;border-radius:16px;font-size:12px;font-weight:500;color:#fff}
.btn-login{left:879px;top:23px;width:96px;height:31px;background:var(--blue)}
.btn-book{left:983px;top:23px;width:128px;height:31px;background:#4a4a4d}
.nav{left:549px;top:78px;display:flex;font-size:14px;font-weight:500;color:var(--ink)}
.nav a{color:inherit;text-decoration:none;margin-right:44px}
.nav a.current{color:var(--blue)}
.nav a:last-child{margin-right:0}

/* hero */
.hero{left:0;top:120px;width:1200px;height:670px;overflow:hidden}
.hero-photo{position:absolute;inset:0;background:linear-gradient(110deg,#bfc3c6 0%,#9aa3ab 35%,#5c7fa8 60%,#8294a6 85%,#b8bec4 100%)}
.hero-shade{position:absolute;inset:0;background:rgba(30,34,45,.28)}
.hero-eyebrow{left:0;top:192px;width:1200px;text-align:center;color:#fff;font-size:18px;font-weight:400;letter-spacing:.3px}
.hero-title{left:0;top:222px;width:1200px;text-align:center;color:#fff;font-size:38px;font-weight:600;line-height:46px}
.btn-hero{left:536px;top:334px;width:128px;height:31px;background:var(--blue);font-size:12px}
.hero-arrow{top:248px}
.hero-wave{left:0;top:480px}

/* section headings */
.heading{left:0;width:1200px;display:flex;justify-content:center;align-items:center;gap:24px;font-size:36px;font-weight:400;color:var(--ink)}
.heading span{color:var(--blue)}
.heading i{display:block;width:86px;height:3px;background:var(--line)}

/* service cards */
.card{width:376px}
.card-photo{height:201px;border-bottom:3px solid var(--blue)}
.card-title{margin:30px 0 0 24px;font-size:15px;font-weight:500}
.card-text{margin:14px 30px 0 24px;font-size:11.5px;line-height:17.5px;color:var(--grey)}
.read-more{display:flex;align-items:center;gap:6px;font-size:12px;font-weight:500;color:var(--grey)}
.read-more.active{color:var(--blue)}
.card .read-more{margin:24px 0 0 24px}

/* about */
.about-title{left:87px;top:1336px;font-size:36px;font-weight:400;display:flex;align-items:center;gap:22px}
.about-title span{color:var(--blue)}
.about-title i{display:block;width:86px;height:3px;background:var(--line)}
.about-lead{left:87px;top:1408px;width:520px;font-size:16.5px;font-weight:500;line-height:22px}
.about-text{left:87px;top:1474px;width:566px;font-size:11.5px;line-height:17.6px;color:var(--grey)}
.btn-discover{left:87px;top:1604px;width:129px;height:31px;background:#4a4a4d}

/* why choose */
.why{left:0;top:1756px;width:1200px;height:560px;background:linear-gradient(135deg,#efeff0,#f7f7f8 50%,#ececee)}
.feature{width:220px;text-align:center}
.feature-title{font-size:15px;font-weight:500;line-height:18px;margin-top:14px}
.feature-title.active{color:var(--blue)}
.feature-text{margin-top:18px;font-size:11.5px;line-height:17.6px;color:var(--grey)}
.feature .read-more{justify-content:center;margin-top:18px}

/* estimate form */
.field{height:31px;border:1px solid var(--field);border-radius:16px;font-size:10.5px;color:var(--muted);padding:9px 16px}
.field.area{height:104px;border-radius:14px}
.btn-submit{left:553px;top:2671px;width:95px;height:31px;background:var(--blue)}

/* footer */
.footer{left:0;top:2800px;width:1200px;height:506px}
.footer-bg{position:absolute;left:0;top:50px;width:1200px;height:456px;background:linear-gradient(160deg,#444447,#323235)}
.f-head{font-size:15px;font-weight:500;color:#fff}
.f-call{font-family:"Oswald",sans-serif;font-weight:300;font-size:17px;color:#fff;display:flex;gap:6px;align-items:center}
.f-small{font-size:11.5px;color:#c9c9cc;line-height:17px}
.f-name{font-size:12px;font-weight:600;color:#fff}
.f-links{list-style:none;font-size:11.5px;color:#c9c9cc}
.f-links li{height:29px}
.social{width:26px;height:26px;border-radius:50%;border:1px solid #6b6b6f}
.social.active{background:var(--blue);border-color:var(--blue)}
.map{left:616px;top:2922px;width:495px;height:239px;background:linear-gradient(135deg,#eceded,#e2e3e4)}
.copyright{font-size:11.5px;color:#c9c9cc}
.copyright b{color:#fff;font-weight:500}
</style>
</head>
<body>

<header class="site-header">
  <div class="abs brand"><div class="brand-dot"></div><div class="brand-name">MARGOT'S CLEANING SERVICE</div></div>
  <div class="abs call">Call Us:
    <svg width="15" height="15" viewBox="0 0 24 24" fill="none" stroke="#2447a0" stroke-width="2"><path d="M22 16.9v3a2 2 0 0 1-2.2 2 19.8 19.8 0 0 1-8.6-3.1 19.5 19.5 0 0 1-6-6A19.8 19.8 0 0 1 2.1 4.2 2 2 0 0 1 4.1 2h3a2 2 0 0 1 2 1.7c.1 1 .4 1.9.7 2.8a2 2 0 0 1-.5 2.1L8 9.9a16 16 0 0 0 6 6l1.3-1.3a2 2 0 0 1 2.1-.4c.9.3 1.8.6 2.8.7a2 2 0 0 1 1.7 2z"/></svg>
    +123-555-0147</div>
  <div class="abs btn btn-login">
    <svg width="11" height="11" viewBox="0 0 24 24" fill="none" stroke="#fff" stroke-width="2.4" style="margin-right:6px"><circle cx="12" cy="8" r="4"/><path d="M4 21c0-4 4-6 8-6s8 2 8 6"/></svg>Login</div>
  <div class="abs btn btn-book">Book Now!</div>
  <nav class="abs nav">
    <a class="current" href="#">-- Home --</a><a href="#">About Us</a><a href="#">Services</a><a href="#">Statement of Faith</a><a href="#">Contact Us</a>
  </nav>
</header>

<section class="abs hero">
  <div class="hero-photo" role="img" aria-label="Gloved hands cleaning a kitchen counter with a spray bottle and cloth"></div>
  <div class="hero-shade"></div>
  <p class="abs hero-eyebrow">MARGOT'S CLEANING SERVICE PROVIDE</p>
  <h1 class="abs hero-title">Residential Move in – Move out and<br>One Time Cleaning Srevices</h1>
  <div class="abs btn btn-hero">Contact Us</div>
  <svg class="abs hero-arrow" style="left:72px" width="18" height="30" viewBox="0 0 18 30" fill="none" stroke="#fff" stroke-width="2"><path d="M15 2 3 15l12 13"/></svg>
  <svg class="abs hero-arrow" style="left:1110px" width="18" height="30" viewBox="0 0 18 30" fill="none" stroke="#fff" stroke-width="2"><path d="M3 2l12 13L3 28"/></svg>
  <svg class="abs" style="left:589px;top:480px" width="22" height="18" viewBox="0 0 22 18" fill="none" stroke="#fff" stroke-width="1.6"><path d="M3 2l8 7 8-7M3 9l8 7 8-7"/></svg>
  <svg class="abs hero-wave" width="1200" height="190" viewBox="0 0 1200 190">
    <path d="M0 150 C 250 225 480 150 700 85 C 900 30 1080 40 1200 80 L1200 190 L0 190Z" fill="#2447a0"/>
    <path d="M0 128 C 250 205 480 170 700 110 C 900 58 1080 60 1200 96 L1200 190 L0 190Z" fill="#f4f4f5"/>
    <path d="M0 128 C 260 190 500 205 720 150 C 900 100 1080 95 1200 110 L1200 190 L0 190Z" fill="#fff" opacity="0"/>
  </svg>
</section>

<h2 class="abs heading" style="top:798px"><i></i>Our&nbsp;<span>Services</span><i></i></h2>

<article class="abs card" style="left:208px;top:875px">
  <div class="card-photo" role="img" aria-label="Stacked moving boxes in a bright living room" style="background:linear-gradient(135deg,#d9d6d0,#c49a6b 55%,#b8885a)"></div>
  <h3 class="card-title" style="color:var(--blue)">Move In – Move Out</h3>
  <p class="card-text">We understand that moving is a daunting process and we are delighted to offer services if that means less stress for you. From ceiling to floor, we will take care of it! ...</p>
  <div class="read-more active">Read More <span>→</span></div>
</article>

<article class="abs card" style="left:616px;top:875px">
  <div class="card-photo" role="img" aria-label="Person in blue gloves spraying and wiping a kitchen counter" style="background:linear-gradient(135deg,#cfd4d2,#8fb6c6 50%,#3f9bd2)"></div>
  <h3 class="card-title">One Time Cleaning</h3>
  <p class="card-text">Planning a party, hosting the in-laws, or just too busy to clean this week? We've got you covered! We offer our detailed cleaning expertise to those who aren't looking ...</p>
  <div class="read-more">Read More <span>→</span></div>
</article>

<h2 class="abs about-title">About&nbsp;<span>Us</span><i></i></h2>
<p class="abs about-lead">Margot's Cleaning Service is a faith based cleaning business founded in middle Tennessee over 19 years ago.</p>
<p class="abs about-text">Fueled by great work and word of mouth, a part time source of income to a mother of 4 changed and grew by into a full time job. Over the years Margot's Cleaning Service has developed its cleaning process into a methodical approach where attention to detail and a continual striving for excellence presents itself in everything we do. We realize that life gets busy and sometimes cleaning is a tall hurdle to overcome, so we consider it an honor if we get to help make life a little easier ...</p>
<div class="abs btn btn-discover">Discover More</div>

<svg class="abs" style="left:715px;top:1298px" width="400" height="400" viewBox="0 0 400 400">
  <path d="M 24 190 A 176 176 0 0 1 340 90" fill="none" stroke="#4a4a4d" stroke-width="9"/>
  <path d="M 310 42 A 180 180 0 0 1 392 195" fill="none" stroke="#2447a0" stroke-width="6"/>
  <path d="M 50 325 A 190 190 0 0 0 350 330" fill="none" stroke="#4a4a4d" stroke-width="9"/>
  <path d="M 80 340 A 170 170 0 0 0 348 318" fill="none" stroke="#2447a0" stroke-width="6"/>
  <circle cx="200" cy="200" r="167" fill="#c9ccd3"/>
</svg>
<div class="abs" role="img" aria-label="Person in yellow gloves vacuuming a carpet" style="left:748px;top:1331px;width:334px;height:334px;border-radius:50%;background:linear-gradient(150deg,#e3e4e8,#b9c0cc 45%,#e2dccd)"></div>

<section class="abs why">
  <svg class="abs" style="left:0;top:480px" width="1200" height="110" viewBox="0 0 1200 110">
    <path d="M0 70 C 200 120 420 90 650 45 C 850 8 1050 15 1200 45 L1200 110 L0 110Z" fill="#2447a0"/>
    <path d="M0 62 C 220 122 430 105 650 62 C 850 22 1050 30 1200 60 L1200 110 L0 110Z" fill="#fff"/>
  </svg>
</section>
<h2 class="abs heading" style="top:1829px"><i></i>Why Choose&nbsp;<span>Us</span><i></i></h2>

<div class="abs feature" style="left:91px;top:1900px">
  <svg width="110" height="110" viewBox="0 0 110 110"><path d="M12 68 A 44 44 0 0 1 98 68" fill="none" stroke="#3f3f42" stroke-width="4" stroke-dasharray="0"/><path d="M22 86 A 44 44 0 0 0 88 86" fill="none" stroke="#2447a0" stroke-width="4"/><rect x="38" y="38" width="26" height="32" rx="3" fill="#2447a0"/><path d="M66 70 L76 38" stroke="#2447a0" stroke-width="4"/></svg>
  <h3 class="feature-title">We Supply<br>Everything</h3>
  <p class="feature-text">Margot's Cleaning Service provides all equipment and cleaning supplies needed to clean your home to the highest standards ...</p>
  <div class="read-more">Read More <span>→</span></div>
</div>
<div class="abs feature" style="left:355px;top:1900px">
  <svg width="110" height="110" viewBox="0 0 110 110"><path d="M12 68 A 44 44 0 0 1 98 68" fill="none" stroke="#3f3f42" stroke-width="4"/><path d="M22 86 A 44 44 0 0 0 88 86" fill="none" stroke="#2447a0" stroke-width="4"/><rect x="34" y="52" width="10" height="22" rx="2" fill="#2447a0"/><path d="M47 52 L56 34 Q62 34 61 44 L60 50 H74 Q78 52 76 58 L72 72 Q70 75 66 75 H47Z" fill="#2447a0"/></svg>
  <h3 class="feature-title active">Statement of<br>Faith</h3>
  <p class="feature-text">As a faith based business Margot's Cleaning Service clings to Colossians 3:23 " And whatsoever ye do, do it heartily as ...</p>
  <div class="read-more active">Read More <span>→</span></div>
</div>
<div class="abs feature" style="left:619px;top:1900px">
  <svg width="110" height="110" viewBox="0 0 110 110"><path d="M12 68 A 44 44 0 0 1 98 68" fill="none" stroke="#3f3f42" stroke-width="4"/><path d="M22 86 A 44 44 0 0 0 88 86" fill="none" stroke="#2447a0" stroke-width="4"/><rect x="32" y="52" width="46" height="20" rx="3" fill="#2447a0"/><circle cx="40" cy="76" r="4" fill="#2447a0"/><circle cx="70" cy="76" r="4" fill="#2447a0"/><rect x="50" y="34" width="10" height="16" rx="2" fill="#2447a0"/></svg>
  <h3 class="feature-title">Highly Trained,<br>and Screened Employees</h3>
  <p class="feature-text">Our professional house cleaners are held to very high standards not only in cleaning, but social performance as well ...</p>
  <div class="read-more">Read More <span>→</span></div>
</div>
<div class="abs feature" style="left:882px;top:1900px">
  <svg width="110" height="110" viewBox="0 0 110 110"><path d="M12 68 A 44 44 0 0 1 98 68" fill="none" stroke="#3f3f42" stroke-width="4"/><path d="M22 86 A 44 44 0 0 0 88 86" fill="none" stroke="#2447a0" stroke-width="4"/><text x="55" y="72" text-anchor="middle" font-family="Poppins,sans-serif" font-weight="600" font-size="44" fill="#2447a0">$</text></svg>
  <h3 class="feature-title">Surprisingly<br>Affordable</h3>
  <p class="feature-text">At Margot's Cleaning Service we are often able to offer our high quality cleaning services at lower cost than our big company ...</p>
  <div class="read-more">Read More <span>→</span></div>
</div>

<h2 class="abs heading" style="top:2421px"><i></i>Get A&nbsp;<span>Free Esstimate</span><i></i></h2>
<div class="abs field" style="left:208px;top:2497px;width:248px">Your Name</div>
<div class="abs field" style="left:476px;top:2497px;width:248px">Email</div>
<div class="abs field" style="left:744px;top:2497px;width:248px">Phone</div>
<div class="abs field area" style="left:208px;top:2549px;width:784px">Message ...</div>
<div class="abs btn btn-submit">Submit</div>

<footer class="abs footer">
  <svg class="abs" style="left:0;top:0" width="1200" height="60" viewBox="0 0 1200 60">
    <path d="M0 10 C 250 -5 520 40 760 40 C 960 40 1100 10 1200 -2 L1200 60 L0 60Z" fill="#2447a0"/>
    <path d="M0 20 C 250 8 520 58 760 56 C 960 54 1100 24 1200 12 L1200 60 L0 60Z" fill="#3f3f42"/>
  </svg>
  <div class="footer-bg"></div>
</footer>
<h4 class="abs f-head" style="left:87px;top:2918px">Quick Links</h4>
<div class="abs f-call" style="left:87px;top:2964px">Call Us:
  <svg width="15" height="15" viewBox="0 0 24 24" fill="none" stroke="#fff" stroke-width="2"><path d="M22 16.9v3a2 2 0 0 1-2.2 2 19.8 19.8 0 0 1-8.6-3.1 19.5 19.5 0 0 1-6-6A19.8 19.8 0 0 1 2.1 4.2 2 2 0 0 1 4.1 2h3a2 2 0 0 1 2 1.7c.1 1 .4 1.9.7 2.8a2 2 0 0 1-.5 2.1L8 9.9a16 16 0 0 0 6 6l1.3-1.3a2 2 0 0 1 2.1-.4c.9.3 1.8.6 2.8.7a2 2 0 0 1 1.7 2z"/></svg>
  +123-555-0147</div>
<p class="abs f-small" style="left:87px;top:2990px">e. info@margotclean.com</p>
<p class="abs f-name" style="left:87px;top:3027px">Margot's Cleaning Service</p>
<p class="abs f-small" style="left:87px;top:3052px">4410 Maple Grove Road Harlow,<br>TN 37201</p>
<div class="abs social" style="left:91px;top:3133px"></div>
<div class="abs social active" style="left:129px;top:3133px"></div>
<div class="abs social" style="left:168px;top:3133px"></div>

<h4 class="abs f-head" style="left:436px;top:2918px">Quick Links</h4>
<ul class="abs f-links" style="left:436px;top:2964px">
  <li>Home</li><li>About Us</li><li>Services</li><li>Statement of Faith</li><li>Contact Us</li><li>Login</li><li>Book Now</li>
</ul>
<div class="abs map" role="img" aria-label="Street map showing the business location"></div>

<p class="abs copyright" style="left:87px;top:3225px">© 2020 <b>Margot's Cleaning Service.</b> All Rights Reseved</p>
<p class="abs copyright" style="left:616px;top:3225px">Privacy Policy &nbsp;&nbsp;&nbsp;|&nbsp;&nbsp;&nbsp; Terms &amp; Conditions</p>

</body>
</html>
```